Corvid Lens Studio Business Card Design

I need a business card designed for a photography business based in Perth, Western Australia called Corvid Lens Studio.

We specialise in wedding, event photography and portrait photography.

The business card must borrow the style of the attached logo.

The hex codes for the colours in the logo are:
#ED1D85 - Pink
#89C23E - Green
#37282F - Black

The name on the card will be:
Name: Tobiah
Phone: 0417395268
Website: www.corvidlensstudio.com.au
Facebook: corvidlensstudio

I am open and happy to accept creative concepts.

Industry/Entity Type

Business

```html
<!DOCTYPE html>
<html lang="en">
<head>
<meta charset="utf-8">
<title>Corvid Lens Studio — Business Card</title>
<link rel="stylesheet" href="https://fonts.googleapis.com/css2?family=Cinzel:wght@400;700&family=Open+Sans:wght@400&display=swap">
<style>
  :root {
    --pink: #ED1D85;
    --green: #89C23E;
    --ink: #37282F;
    --ink-soft: #4a4046;
    --card: #ffffff;
    --backdrop: #a9804f;
    --fb-blue: #3b5998;
  }
  * { margin: 0; padding: 0; box-sizing: border-box; }
  html, body {
    width: 1200px;
    height: 765px;
    overflow: hidden;
  }
  body {
    background: var(--backdrop);
    position: relative;
  }
  .card {
    position: absolute;
    width: 597px;
    height: 340px;
    background: var(--card);
    box-shadow: 0 4px 10px rgba(0, 0, 0, 0.35);
    text-align: center;
  }
  .card--back { left: 534px; top: 360px; }
  .card--front { left: 121px; top: 59px; z-index: 2; }

  .brand-mark {
    position: absolute;
    left: 50%;
    transform: translateX(-50%);
    border-radius: 50%;
    background: var(--pink);
  }
  .card--front .brand-mark { top: 18px; width: 104px; height: 104px; }
  .card--back .brand-mark { top: 78px; width: 118px; height: 118px; }

  .wordmark {
    position: absolute;
    left: 0;
    right: 0;
    font-family: "Cinzel", serif;
    font-weight: 400;
    color: var(--ink-soft);
    white-space: nowrap;
  }
  .card--front .wordmark { top: 152px; font-size: 17px; letter-spacing: 0.58em; padding-left: 0.58em; }
  .card--back .wordmark { top: 223px; font-size: 18px; letter-spacing: 0.6em; padding-left: 0.6em; }

  .holder-name {
    position: absolute;
    top: 212px;
    left: 0;
    right: 0;
    font-family: "Cinzel", serif;
    font-weight: 700;
    font-size: 27px;
    letter-spacing: 0.05em;
    color: var(--ink);
  }
  .contact {
    position: absolute;
    left: 0;
    right: 0;
    display: flex;
    justify-content: center;
    align-items: center;
    gap: 14px;
    font-family: "Open Sans", sans-serif;
    font-size: 15px;
    color: var(--ink-soft);
  }
  .contact--main { top: 258px; }
  .contact--social { top: 288px; }
  .contact__item { display: inline-flex; align-items: center; gap: 6px; }
  .contact__icon { width: 14px; height: 14px; flex: none; }
  .contact__square {
    width: 13px;
    height: 13px;
    background: var(--fb-blue);
    flex: none;
  }
</style>
</head>
<body>

  <section class="card card--back" aria-label="Card back">
    <div class="brand-mark" aria-hidden="true"></div>
    <p class="wordmark">CORVID LENS STUDIO</p>
  </section>

  <section class="card card--front" aria-label="Card front">
    <div class="brand-mark" aria-hidden="true"></div>
    <p class="wordmark">CORVID LENS STUDIO</p>
    <h1 class="holder-name">Tobiah</h1>

    <div class="contact contact--main">
      <span class="contact__item">
        <svg class="contact__icon" viewBox="0 0 14 14" aria-hidden="true">
          <circle cx="7" cy="7" r="6.3" fill="none" stroke="var(--pink)" stroke-width="1.2"/>
          <path d="M4.6 3.8 L5.9 3.6 L6.4 5.3 L5.6 6 Q6.3 7.7 8 8.4 L8.7 7.6 L10.4 8.1 L10.2 9.4 Q6 10 4.6 3.8 Z" fill="var(--pink)"/>
        </svg>
        0417395268
      </span>
      <span class="contact__item">
        <svg class="contact__icon" viewBox="0 0 14 14" aria-hidden="true">
          <g fill="none" stroke="var(--pink)" stroke-width="1.1">
            <circle cx="7" cy="7" r="6"/>
            <ellipse cx="7" cy="7" rx="2.6" ry="6"/>
            <line x1="1" y1="7" x2="13" y2="7"/>
            <path d="M2.2 4 H11.8 M2.2 10 H11.8"/>
          </g>
        </svg>
        www.corvidlensstudio.com.au
      </span>
    </div>

    <div class="contact contact--social">
      <span class="contact__item">
        <span class="contact__square" aria-hidden="true"></span>
        corvidlensstudio
      </span>
    </div>
  </section>

</body>
</html>
```